Luxury Wine Label for New Startup Winery

We need a wine label for our new winery startup. We have worked with a local designer but do not feel the resulting label / logo have the elevation required to present our brand as a luxury wine. Our winery is called "Harrowgate Vineyards" and we are focused on extremely high quality hand crafted artisan and estate wines from the Pacific Northwest.
We would like to see designs that utilize a tree line, or other imagery that represents the "Harrowgate" part of our company name. Another interesting feature could be wood grain.
A logo will be required based on your design so please design with this in mind:
This logo should be consistent with the wine bottle label design, and should be representative of our high end exclusive wine while giving a sense of place (Oregon/ Pacific Northwest.)
I will supply an image of the design we received from our local designer, PLEASE NOTE: in general we do like wood grain and tree line concepts but feel the execution was poorly done.
ATTN: Logo design should be suitable for use on: Bottles (Red wine/rose/white wine), Bussiness cards, vehicle signage, business signage, etc
P.S.:
If you have a design that is not outside the box we are still interested in seeing it.
Label is for a burgundy style bottle with a label height of 3.5 - 4" and a width of 3.5-4"
any label <= 4"x4" and >=3.5"x3.5" will be acceptable:
HOWEVER Width should be greater than or equal to height due to the bottle format
Target Market(s)
Wine enthusiasts with adequate discretionary budgets to afford $100 bottles of wine.
Industry/Entity Type
Wine / Winery
Requirements
Must have
- A sense of luxury, a feel of exclusivity, and a theme consistent with our product and brand name
Nice to have
- Tree line, wood grain or other wood themes. Serif fonts
Should not have
- anything cheesy, off topic, hard to read script fonts or anything that makes the label hard to read from a few feet away or too busy

```html
<!DOCTYPE html>
<html lang="en">
<head>
<meta charset="utf-8">
<title>Harrowgate Vineyards – Willamette Valley Syrah Label</title>
<link rel="stylesheet" href="https://fonts.googleapis.com/css2?family=Cormorant+Garamond:wght@500;600&family=Great+Vibes&display=swap">
<style>
  :root {
    --page-bg: #ece7df;
    --label-paper: #f5f2ed;
    --grain-light: #ebe6df;
    --grain-dark: #d9d3cb;
    --gold: #b9974a;
    --gold-light: #d8bd78;
    --wine-red: #c8202c;
    --ink: #2b2724;
    --tree-dark: #5e5138;
  }
  * { margin: 0; padding: 0; box-sizing: border-box; }
  html, body {
    width: 800px;
    height: 1200px;
    overflow: hidden;
    background: var(--page-bg);
  }
  .canvas {
    position: relative;
    width: 800px;
    height: 1200px;
  }
  .wine-label {
    position: absolute;
    left: 80px;
    top: 290px;
    width: 640px;
    height: 620px;
    background: var(--label-paper);
    overflow: hidden;
    box-shadow: 0 2px 10px rgba(0,0,0,0.08);
  }
  .wood-grain {
    position: absolute;
    inset: 0;
    background: linear-gradient(168deg, var(--grain-light) 0%, var(--label-paper) 40%, var(--grain-dark) 100%);
  }
  .gold-swoosh {
    position: absolute;
    left: 0;
    top: 0;
    width: 640px;
    height: 160px;
  }
  .label-content {
    position: absolute;
    inset: 0;
    text-align: center;
    color: var(--ink);
    font-family: "Cormorant Garamond", serif;
    font-weight: 500;
  }
  .label-content p,
  .label-content h1 {
    position: absolute;
    left: 0;
    right: 0;
    line-height: 1;
  }
  .brand-name {
    top: 172px;
    font-weight: 500;
    font-size: 40px;
    letter-spacing: 1px;
    color: var(--ink);
  }
  .region {
    top: 248px;
    font-family: "Great Vibes", cursive;
    font-size: 64px;
    color: var(--wine-red);
  }
  .varietal {
    top: 336px;
    font-size: 44px;
    letter-spacing: 3px;
  }
  .vintage {
    top: 390px;
    font-size: 32px;
    letter-spacing: 2px;
  }
  .edition {
    top: 430px;
    font-size: 32px;
    letter-spacing: 2px;
  }
  .estate-note {
    top: 472px;
    font-weight: 600;
    font-size: 15px;
    letter-spacing: 1px;
  }
  .tree-line {
    position: absolute;
    left: 0;
    right: 0;
    bottom: 0;
    height: 230px;
    background: linear-gradient(180deg, rgba(138,122,88,0) 0%, rgba(138,122,88,0.55) 45%, var(--tree-dark) 100%);
  }
</style>
</head>
<body>
  <main class="canvas">
    <section class="wine-label">
      <div class="wood-grain" role="img" aria-label="Pale silvery wood grain texture across the label"></div>

      <svg class="gold-swoosh" viewBox="0 0 640 160" aria-hidden="true">
        <path d="M0 40 Q 320 70 640 150" fill="none" stroke="var(--gold)" stroke-width="3"/>
        <path d="M0 50 Q 320 80 640 160" fill="none" stroke="var(--gold-light)" stroke-width="1.5"/>
      </svg>

      <div class="tree-line" role="img" aria-label="Silhouetted evergreen tree line along the bottom of the label"></div>

      <div class="label-content">
        <h1 class="brand-name">HARROWGATE VINEYARDS</h1>
        <p class="region">Willamette Valley</p>
        <p class="varietal">SYRAH</p>
        <p class="vintage">2024</p>
        <p class="edition">LIMITED EDITION</p>
        <p class="estate-note">ESTATE GROWN | HANDCRAFTED</p>
      </div>
    </section>
  </main>
</body>
</html>
```